A Dedicated Thank You to my Dad

Proposed Dimensions: Approx. 20" x 30"

For Father's Day, I wrote a dedication to my Dad that encapsulates my gratitude for everything he does, and everything he is. His birthday is on August 3, but it is more important for me to transform this dedication into a meaningful and memorable gift than to meet any deadline. I would love an image that captures the relationship between a father and his son, accompanied by my words of thanks in some sort of font that is appropriate for the message (calligprahy? not sure about that).

I had actually posted the Thank You on Chatterloop as a public post, so anyone with an account can read it: https://www.chatterloop.example/photo.php?fbid=20473819265038417&set=a.918364027159.5829361.3940582&type=1&theater

Only the words starting with "Thank you ..." should be on the poster.

Target Market(s)

This is a personal gift for my Dad. He doesn't have the best of eyesight, so having the words in a really small font would not be particularly helpful. :-)

Requirements
Must have
• * Personable
* Warm
* Inviting
* Memorable
* Understated more favored over Loud
Should not have
• * An entire palette of colors
* Wacky colors or fonts

```html
<!DOCTYPE html>
<html lang="en">
<head>
<meta charset="utf-8">
<title>Thank You Dad!!</title>
<link rel="stylesheet" href="https://fonts.googleapis.com/css2?family=EB+Garamond:wght@600&family=Playfair+Display:ital,wght@1,900&display=swap">
<style>
  :root {
    --sky-top: #6b3512;
    --sky-mid: #c2701f;
    --sun-core: #fff3c4;
    --sun-glow: #f7b548;
    --sea-dark: #3a1a08;
    --ground-deep: #1e0c04;
    --title-gold: #f6c84a;
    --title-edge: #0f0702;
    --verse-ink: #3a1a07;
    --verse-glow: rgba(255, 190, 95, 0.95);
  }
  html, body {
    margin: 0;
    padding: 0;
    width: 776px;
    height: 1200px;
    overflow: hidden;
    background: var(--ground-deep);
  }
  .poster {
    position: relative;
    width: 776px;
    height: 1200px;
    overflow: hidden;
  }
  .sunset-scene {
    position: absolute;
    inset: 0;
    background:
      radial-gradient(ellipse 150px 70px at 600px 192px, var(--sun-core) 0%, rgba(255, 230, 150, 0.7) 35%, rgba(247, 181, 72, 0) 100%),
      radial-gradient(ellipse 420px 260px at 600px 200px, rgba(247, 181, 72, 0.9) 0%, rgba(214, 128, 40, 0.55) 45%, rgba(160, 80, 25, 0) 100%),
      linear-gradient(180deg, var(--sky-top) 0%, var(--sky-mid) 13%, #d88b35 17%, #a75a22 28%, #7a3d17 45%, var(--sea-dark) 70%, var(--ground-deep) 100%);
  }
  .title {
    position: absolute;
    left: 34px;
    top: 26px;
    margin: 0;
    font-family: "Playfair Display", Georgia, serif;
    font-style: italic;
    font-weight: 900;
    font-size: 56px;
    line-height: 1;
    letter-spacing: -0.5px;
    color: var(--title-gold);
    -webkit-text-stroke: 1.5px var(--title-edge);
    text-shadow: 2px 3px 4px rgba(0, 0, 0, 0.85), 0 0 10px rgba(0, 0, 0, 0.5);
  }
  .verses {
    position: absolute;
    left: 32px;
    top: 106px;
    width: 740px;
    margin: 0;
    padding: 0;
    list-style: none;
    font-family: "EB Garamond", Georgia, serif;
    font-weight: 600;
    font-size: 18.6px;
    line-height: 24.6px;
    letter-spacing: -0.15px;
    color: var(--verse-ink);
    text-shadow: 0 0 3px var(--verse-glow), 0 0 6px var(--verse-glow), 0 0 2px var(--verse-glow);
    white-space: nowrap;
  }
  .verses li { margin: 0; }
</style>
</head>
<body>
<main class="poster">
  <div class="sunset-scene" role="img" aria-label="Photograph of a beach at sunset with a father and his young son walking hand in hand along the shore"></div>
  <h1 class="title">Thank You Dad!!</h1>
  <ul class="verses">
    <li>Thank you for, after the initial shock, embracing the unexpected news that you were about to<br>have twins.</li>
    <li>Thank you for buying enough diapers to single-handedly enable B &amp; K to make a profit.</li>
    <li>Thank you for always carrying us to the car after we fell asleep, even after we were definitely<br>old enough to walk it.</li>
    <li>Thank you for not telling on us when<br>&nbsp;we were only pretending to nap.</li>
    <li>Thank you for welcoming more people to<br>stay with us than I can count.</li>
    <li>Thank you for sitting through more howings of “Jukebox”<br>and “Galaxy Raiders” than any human should endure.</li>
    <li>Thank you for doggedly trying to teach me that the beach is not<br>to be feared nor cleaned.</li>
    <li>Thank you for working two jobs, for years, to make ends meet.</li>
    <li>Thank you for loading us all up in the station wagon, pillows in tow, so we could watch the<br>first drive-in movie together and squint in the second.</li>
    <li>Thank you for, as coach, letting me take a fake rabbit’s foot onto the soccer field.</li>
    <li>Thank you for being willing to put a hit out on my guitar teacher when he beat feet.</li>
    <li>Thank you for letting me sing in my room as if I were the originating artist.</li>
    <li>Thank you for making car trips with you, wherever we were going, fun and special.</li>
    <li>Thank you for proudly and patiently taking me to my first nerd conference in junior high.</li>
    <li>Thank you for putting up with the commutes you did, for decades, so we could grow up<br>amongst family in an incredible community.</li>
    <li>Thank you for my dry sense of humor. I cherish it.</li>
    <li>Thank you for finding a way, by hook or by crook, to send three children to college at the<br>same time, and to allow me to go to the college of my dreams.</li>
    <li>Thank you for never giving up on trying to convince me that imperfection is not a failure.</li>
    <li>Thank you for mispronouncing, I believe on purpose, pop culture references in a way that<br>only you can.</li>
    <li>Thank you for teaching me to try to find the good in everyone.</li>
    <li>Thank you for waiting to laugh out loud with Mom until after the police left when my camp<br>friends and I apparently made too much noise.</li>
    <li>Thank you for showing me that there is peace to be found in stillness and quiet.</li>
    <li>Thank you for demonstrating the fun that can be had and the truths that can be gleaned<br>from philosophical and political debate.</li>
    <li>Thank you for accepting me for who I am, no matter who I love, and for helping me to accept<br>myself.</li>
    <li>Thank you for doing whatever you can to help whoever you can, whether friend, family or<br>stranger.</li>
    <li>Thank you for trusting me enough to let your guard sometimes to let me know how you are<br>truly doing.</li>
    <li>Thank you for insisting, year after year, that time with you means more than any gift I could<br>ever purchase. That is one lesson, amongst so many, that I will pass down to our next<br>generation</li>
  </ul>
</main>
</body>
</html>
```